Fresh Produce Outlet needs a Poster Design

Hi,
We are Brightleaf Harvest Market, a fruit and veg outlet based in the suburb of Yanchep, Perth, Western Australia.Apart from fresh produce, we also stock nuts and grains, organic products and specialty grocery. We are about to launch a re-branding exercise, projecting ourselves as 'the' shop for fresh produce; quality, taste and freshness being our key differentiators. We are competing against a big supermarket chain who are using marketing muscle power to shut us down and we want to respond with a series of posters which are simple yet bold and sends a clear and positive message to our customers about what we have to offer.
Please feel free to visit our Facebook page www.facebook.com/brightleafharvestmkt to get an idea about our current branding,logo and the shop in general.
Regards
Team - Brightleaf Harvest Market
Target Market(s)
Residents of Yanchep and surrounding suburbs
Industry/Entity Type
Retail
Look and feel

```html
<!DOCTYPE html>
<html lang="en">
<head>
<meta charset="utf-8">
<title>Brightleaf Harvest Market – Taste Poster</title>
<link rel="stylesheet" href="https://fonts.googleapis.com/css2?family=Dosis:wght@400;500;700&display=swap">
<style>
  :root {
    --page-bg: #eeeeee;
    --poster-white: #ffffff;
    --ray-peach: #fbe3cc;
    --brand-green: #2f9a3e;
    --accent-orange: #f0a052;
    --band-orange: #f3ad6a;
    --tick-red: #e0262b;
    --grain-dark: #6b4424;
    --grain-mid: #a8744a;
    --grain-light: #d9b98a;
    --text-white: #ffffff;
  }
  * { margin: 0; padding: 0; box-sizing: border-box; }
  html, body {
    width: 1200px;
    height: 1000px;
    overflow: hidden;
    background: var(--page-bg);
    font-family: "Dosis", "Trebuchet MS", sans-serif;
  }
  .poster {
    position: absolute;
    left: 320px;
    top: 50px;
    width: 560px;
    height: 900px;
    overflow: hidden;
    background:
      radial-gradient(ellipse at 50% 34%, var(--poster-white) 0%, var(--poster-white) 25%, var(--ray-peach) 100%);
    box-shadow: 0 4px 18px rgba(0,0,0,0.15);
  }
  .brand-name {
    position: absolute;
    top: 70px;
    left: 0;
    width: 100%;
    text-align: center;
    font-weight: 700;
    font-size: 28px;
    color: var(--brand-green);
    letter-spacing: 0.3px;
  }
  .brand-name .brand-dot {
    display: inline-block;
    width: 14px;
    height: 14px;
    border-radius: 50%;
    background: var(--brand-green);
    margin-right: 10px;
    vertical-align: 2px;
  }
  .headline {
    position: absolute;
    top: 220px;
    left: 130px;
    display: flex;
    align-items: center;
    gap: 60px;
  }
  .headline .tick-box { width: 78px; height: 88px; }
  .headline .headline-word {
    font-weight: 400;
    font-size: 62px;
    color: var(--accent-orange);
    font-variant: small-caps;
    letter-spacing: 2px;
    margin-top: 24px;
  }
  .produce-photo {
    position: absolute;
    left: 0;
    top: 440px;
    width: 560px;
    height: 360px;
    background:
      radial-gradient(ellipse at 20% 20%, var(--grain-mid) 0%, transparent 45%),
      radial-gradient(ellipse at 75% 75%, var(--grain-light) 0%, transparent 50%),
      radial-gradient(ellipse at 35% 80%, var(--grain-light) 0%, transparent 40%),
      linear-gradient(135deg, var(--grain-dark) 0%, var(--grain-mid) 55%, var(--grain-light) 100%);
  }
  .arc-band {
    position: absolute;
    left: 0;
    top: 360px;
    width: 560px;
    height: 120px;
  }
  .footer-bar {
    position: absolute;
    left: 0;
    bottom: 0;
    width: 560px;
    height: 100px;
    background: var(--accent-orange);
    color: var(--text-white);
  }
  .footer-bar .web-address {
    position: absolute;
    left: 22px;
    top: 14px;
    font-size: 14px;
    font-weight: 500;
  }
  .footer-bar .tagline {
    position: absolute;
    right: 22px;
    bottom: 16px;
    font-size: 36px;
    font-weight: 400;
    font-variant: small-caps;
    letter-spacing: 1px;
  }
</style>
</head>
<body>
  <main class="poster">
    <div class="brand-name"><span class="brand-dot"></span>Brightleaf Harvest Market</div>

    <div class="headline">
      <svg class="tick-box" viewBox="0 0 78 88" aria-hidden="true">
        <rect x="4" y="26" width="56" height="56" rx="6" fill="none" stroke="var(--brand-green)" stroke-width="6"/>
        <path d="M16 50 L30 68 Q44 30 74 6 Q48 36 31 58 Z" fill="var(--tick-red)"/>
        <path d="M12 48 L20 44 L32 62 Z" fill="var(--tick-red)"/>
      </svg>
      <span class="headline-word">Taste</span>
    </div>

    <div class="produce-photo" role="img" aria-label="Photo of wholegrain bread slices, a muffin in a hessian-lined basket, wheat ears, rolled oats, bran flakes and a bowl of grains on a wooden board"></div>

    <svg class="arc-band" viewBox="0 0 560 120" aria-hidden="true">
      <path d="M0 70 Q280 -10 560 70 L560 110 Q280 50 0 110 Z" fill="var(--band-orange)"/>
    </svg>

    <footer class="footer-bar">
      <span class="web-address">www.brightleafharvest.com.au</span>
      <span class="tagline">The Shop for Fresh Produce</span>
    </footer>
  </main>
</body>
</html>
```